pathology learning flashcard template graphic design .

Creative designs for 2 sides of the flashcards to include colorful sectioning and font sizes that will make it easy to use in studying.

```html
<!DOCTYPE html>
<html lang="en">
<head>
<meta charset="utf-8">
<title>Pathology Flashcard – Case 0001</title>
<link href="https://fonts.googleapis.com/css2?family=Comic+Neue:wght@400;700&display=swap" rel="stylesheet">
<style>
  :root {
    --navy: #0b4a7c;
    --sky-top: #7fdcf2;
    --sky-mid: #c2eef8;
    --sky-bottom: #ffffff;
    --ink: #1b1b1b;
    --letter: #1f5fa8;
    --card-fill: #f4efe9;
    --card-border: #0b4a7c;
  }
  * { margin: 0; padding: 0; box-sizing: border-box; }
  html, body { width: 720px; height: 1200px; overflow: hidden; }
  body {
    font-family: "Comic Neue", "Comic Sans MS", cursive;
    color: var(--ink);
    background: var(--sky-bottom);
  }
  .flashcard {
    position: relative;
    width: 720px;
    height: 1200px;
    background: linear-gradient(180deg, var(--sky-top) 0%, var(--sky-mid) 38%, #e6f8fc 62%, var(--sky-bottom) 82%);
    overflow: hidden;
  }
  .case-banner {
    position: absolute;
    left: 0;
    top: 37px;
    width: 466px;
    height: 70px;
  }
  .case-banner svg { position: absolute; inset: 0; }
  .case-title {
    position: absolute;
    left: 22px;
    top: 14px;
    font-size: 35px;
    font-weight: 700;
    color: #ffffff;
    letter-spacing: 0.5px;
    white-space: nowrap;
  }
  .patient-portrait {
    position: absolute;
    left: 216px;
    top: 138px;
    width: 287px;
    height: 365px;
    border: 5px solid var(--card-border);
    border-radius: 22px;
    background: linear-gradient(180deg, #ffffff 0%, var(--card-fill) 55%, #6fa882 100%);
  }
  .case-stem {
    position: absolute;
    left: 22px;
    top: 548px;
    width: 673px;
    font-size: 29px;
    line-height: 34.6px;
    text-align: justify;
    text-align-last: left;
  }
  .answer-options {
    position: absolute;
    left: 24px;
    top: 1052px;
    width: 680px;
    display: grid;
    grid-template-columns: 318px 1fr;
    row-gap: 11px;
    font-size: 28px;
    font-weight: 700;
    list-style: none;
    white-space: nowrap;
  }
  .answer-options .letter { color: var(--letter); margin-right: 6px; }
</style>
</head>
<body>
<main class="flashcard">
  <header class="case-banner">
    <svg width="466" height="70" viewBox="0 0 466 70" aria-hidden="true">
      <polygon points="0,0 466,0 438,70 0,70" fill="var(--navy)"/>
    </svg>
    <h1 class="case-title">Pathology Case ID 0001</h1>
  </header>

  <div class="patient-portrait" role="img" aria-label="Cartoon portrait of an older woman patient with white hair and glasses"></div>

  <p class="case-stem">50-year-old woman comes to the clinic because she has difficulty swallowing for the past few months. She says symptoms have been worsening. She also complains of cough, mostly at night and in fear of choking, has stopped eating many foods, losing about 12 lbs in the past 3 months. Past medical history is unremarkable. Vital signs are normal and physical exam is unremarkable. Chest x-ray with demonstrates an air-fluid level, while manometry shows absent relaxation of the lower esophageal sphincter during swallowing. What is the most likely diagnosis?</p>

  <ol class="answer-options">
    <li><span class="letter">A)</span>GERD</li>
    <li><span class="letter">C)</span>Achalasia</li>
    <li><span class="letter">B)</span>Barret Esophagus</li>
    <li><span class="letter">D)</span>Eosinophilic esophagitis</li>
  </ol>
</main>
</body>
</html>
```